Web Design for Financial Consulting Company

We need a website design for a financial consulting company "Kelvane Consulting". We build financial models, scenario analysis, handle the budgeting process and provide temporary staffing. I have over 10 years of experience. My Excel expertise and analytical savvy has saved clients over $17 million in profit.

Target Market(s)

Small to medium businesses

Industry/Entity Type

Financial Consulting

Number of Pages Required

4 page

Requirements
Must have
• Professional looking
Nice to have
• A little futuristic looking

```html
<!DOCTYPE html>
<html lang="en">
<head>
<meta charset="utf-8">
<title>Kelvane Consulting</title>
<link href="https://fonts.googleapis.com/css2?family=Montserrat:wght@800;900&family=Red+Hat+Display:wght@400;500&family=Inter:wght@400;500;600;700&display=swap" rel="stylesheet">
<style>
:root{
  --bg:#111112;
  --panel:#1d1d1e;
  --footer:#222223;
  --navy:#03466f;
  --accent:#0aa8f2;
  --white:#ffffff;
  --muted:#d6d6d6;
  --line:#2c2c2e;
}
*{margin:0;padding:0;box-sizing:border-box}
html,body{width:1200px;height:3112px;overflow:hidden;background:var(--bg);color:var(--white);font-family:"Inter",sans-serif}
.page{position:relative;width:1200px;height:3112px}
.abs{position:absolute}

/* header */
.hero-bg{left:0;top:0;width:1200px;height:850px;background:radial-gradient(ellipse at 70% 45%,#3a3633 0%,#1f1f22 40%,#121213 80%)}
.hero-photo{left:600px;top:200px;width:533px;height:647px;border-radius:260px 260px 0 0;background:linear-gradient(180deg,#8c7256 0%,#6b5a4c 30%,#2a2a30 60%,#18181c 100%);opacity:.9}
.brand{display:flex;align-items:center;gap:12px}
.brand-mark{width:38px;height:38px;border:3px solid var(--accent)}
.brand-name{font-family:"Inter",sans-serif;font-weight:600;color:var(--white);letter-spacing:2px;line-height:1}
.header-brand{left:0;width:1200px;top:40px;justify-content:center}
.header-brand .brand-name{font-size:30px}
.nav-line{left:330px;width:710px;height:1px;background:var(--line)}
.main-nav{top:141px;left:0;width:1200px;font-size:11px;font-weight:500;letter-spacing:1px}
.main-nav a{position:absolute;color:var(--white);text-decoration:none}
.main-nav .active::after{content:"";position:absolute;left:0;right:0;top:28px;height:3px;background:var(--accent)}

.hero-title{left:122px;top:312px;font-family:"Montserrat",sans-serif;font-weight:900;font-size:58px;line-height:63px;letter-spacing:.5px}
.hero-title .hl{color:var(--accent)}
.hero-sub{left:125px;top:443px;font-family:"Red Hat Display",sans-serif;font-size:31px}
.hero-text{left:125px;top:508px;width:470px;font-size:13px;line-height:22px;color:var(--muted)}
.btn{display:flex;align-items:center;justify-content:center;gap:14px;border-radius:30px;font-size:11px;font-weight:700;text-decoration:none}
.btn svg{width:26px;height:8px}
.btn-outline{left:125px;top:605px;width:240px;height:45px;border:1.5px solid var(--white);color:var(--white)}
.btn-light{background:var(--white);color:var(--navy)}
.btn-navy{background:var(--navy);color:var(--white)}

/* about */
.about{left:125px;top:848px;width:950px;height:440px;background:var(--navy);text-align:center}
.section-title{font-family:"Montserrat",sans-serif;font-weight:900;font-size:41px;line-height:45px}
.section-kicker{font-family:"Red Hat Display",sans-serif;font-size:30px;color:var(--accent)}
.about .section-title{position:absolute;top:68px;width:100%}
.about .section-kicker{position:absolute;top:160px;width:100%}
.about p{position:absolute;top:224px;left:160px;width:630px;font-size:12.5px;line-height:22px;color:#e8eef3}
.about .btn{position:absolute;left:383px;top:324px;width:184px;height:45px}

/* services */
.services-title{left:125px;top:1380px}
.services-kicker{left:125px;top:1474px}
.view-all{left:890px;top:1430px;width:183px;height:45px}
.card{width:222px;height:222px;top:1565px;background:var(--panel);box-shadow:5px 5px 0 #000;text-align:center}
.card .icon{position:absolute;left:81px;top:47px;width:60px;height:60px;border:2px solid var(--accent);border-radius:50%}
.card h3{position:absolute;top:137px;width:100%;font-family:"Inter",sans-serif;font-weight:800;font-size:16.5px;line-height:20px;letter-spacing:.3px}
.card-text{top:1825px;width:180px;font-size:11.5px;line-height:19px;color:var(--muted);text-align:center}

/* contact */
.contact-photo{left:92px;top:2025px;width:491px;height:658px;border-radius:50%;background:radial-gradient(ellipse at 50% 45%,#4d4238 0%,#2c2a2b 45%,#141415 75%)}
.contact-title{left:590px;top:2080px;font-size:40px;line-height:45px}
.contact-kicker{left:590px;top:2225px}
.field{left:590px;width:485px;background:var(--white);color:#333;font-size:11px;padding:14px 20px}
.send{left:892px;top:2657px;width:183px;height:45px}

/* footer */
.footer{left:0;top:2800px;width:1200px;height:312px;background:var(--footer)}
.footer-brand{left:125px;top:2905px}
.footer-brand .brand-mark{width:56px;height:56px}
.footer-brand .brand-name{font-size:46px}
.copyright{left:125px;top:3004px;font-size:15.5px}
.foot-nav{top:2907px;font-size:12.5px;letter-spacing:1px;color:var(--white)}
.social{top:2956px;width:54px;height:54px;border:1.5px solid var(--white);border-radius:50%}
</style>
</head>
<body>
<div class="page">

  <header>
    <div class="abs hero-bg"></div>
    <div class="abs hero-photo" role="img" aria-label="Portrait of a smiling businesswoman in a dark blazer, arms crossed"></div>
    <div class="abs brand header-brand">
      <span class="brand-mark"></span>
      <span class="brand-name">KELVANE CONSULTING</span>
    </div>
    <div class="abs nav-line" style="top:120px"></div>
    <nav class="abs main-nav">
      <a href="#" class="active" style="left:396px">HOME</a>
      <a href="#" style="left:503px">ABOUT</a>
      <a href="#" style="left:615px">SERVICES</a>
      <a href="#" style="left:745px">CONTACT</a>
    </nav>
    <div class="abs nav-line" style="top:177px"></div>

    <h1 class="abs hero-title">HELPING<br>YOUR <span class="hl">FINANCE</span></h1>
    <p class="abs hero-sub">Team And Increasing Profit</p>
    <p class="abs hero-text">Lorem Ipsum is simply dummy text of the printing and typesetting industry. Lorem Ipsum has been the industry's standard dummy text ever since the 1500s,</p>
    <a href="#" class="abs btn btn-outline">Get A Consultant
      <svg viewBox="0 0 26 8"><path d="M0 4h24M20 1l4 3-4 3" fill="none" stroke="#fff" stroke-width="1"/></svg></a>
  </header>

  <section class="abs about">
    <h2 class="section-title">TRANSFORMING<br>IDEAS INTO ACTION</h2>
    <p class="section-kicker">About Kelvane</p>
    <p>I am an experienced Finance professional who develops strategic financial plans, provides insightful analysis, and supports decision-making. With over 10 years of experience, I have successfully increased profitability for clients by $17M.</p>
    <a href="#" class="btn btn-light">Read More
      <svg viewBox="0 0 26 8"><path d="M0 4h24M20 1l4 3-4 3" fill="none" stroke="#03466f" stroke-width="1"/></svg></a>
  </section>

  <section>
    <h2 class="abs section-title services-title">YOUR SUCCESS IS<br>OUR MISSION</h2>
    <p class="abs section-kicker services-kicker">Kelvane Services</p>
    <a href="#" class="abs btn btn-navy view-all">View All
      <svg viewBox="0 0 26 8"><path d="M0 4h24M20 1l4 3-4 3" fill="none" stroke="#fff" stroke-width="1"/></svg></a>

    <div class="abs card" style="left:125px"><span class="icon" role="img" aria-label="Financial report icon"></span><h3>FINANCIAL<br>MODELS</h3></div>
    <div class="abs card" style="left:368px"><span class="icon" role="img" aria-label="Budget gear icon"></span><h3>BUDGETING<br>PROCESS</h3></div>
    <div class="abs card" style="left:610px"><span class="icon" role="img" aria-label="Team icon"></span><h3>TEMPORARY<br>STAFFING</h3></div>
    <div class="abs card" style="left:852px"><span class="icon" role="img" aria-label="Idea and gear icon"></span><h3>PROCESS<br>IMPROVEMENT</h3></div>

    <p class="abs card-text" style="left:146px">Financial analysis, scenario modeling, pricing analysis, projects</p>
    <p class="abs card-text" style="left:389px">Building budgets from scratch, revamping current process to be more robust and scalable.</p>
    <p class="abs card-text" style="left:631px">Years of Financial Planning and Analysis experience across multiple industries can help temporary staffing needs.</p>
    <p class="abs card-text" style="left:873px">Month end close, reporting, budgeting</p>
  </section>

  <section>
    <div class="abs contact-photo" role="img" aria-label="Smiling businessman in glasses talking on a phone"></div>
    <h2 class="abs section-title contact-title">UNLOCK YOUR FULL<br>POTENTIAL WITH OUR<br>EXPERT GUIDANCE</h2>
    <p class="abs section-kicker contact-kicker">Get In Touch With Us</p>
    <div class="abs field" style="top:2292px;height:48px">Name</div>
    <div class="abs field" style="top:2355px;height:48px">Email</div>
    <div class="abs field" style="top:2418px;height:202px">Message</div>
    <a href="#" class="abs btn btn-navy send">Send
      <svg viewBox="0 0 26 8"><path d="M0 4h24M20 1l4 3-4 3" fill="none" stroke="#fff" stroke-width="1"/></svg></a>
  </section>

  <footer>
    <div class="abs footer"></div>
    <div class="abs brand footer-brand">
      <span class="brand-mark"></span>
      <span class="brand-name">KELVANE</span>
    </div>
    <p class="abs copyright">Copyright@2023-Kelvane-Privacy Policy</p>
    <span class="abs foot-nav" style="left:717px">HOME</span>
    <span class="abs foot-nav" style="left:800px">ABOUT</span>
    <span class="abs foot-nav" style="left:891px">SERVICES</span>
    <span class="abs foot-nav" style="left:1002px">CONTACT</span>
    <span class="abs social" style="left:773px" aria-label="Social link"></span>
    <span class="abs social" style="left:856px" aria-label="Social link"></span>
    <span class="abs social" style="left:938px" aria-label="Social link"></span>
    <span class="abs social" style="left:1020px" aria-label="Social link"></span>
  </footer>

</div>
</body>
</html>
```